A poster for Natural Skincare which contains minerals and seaweed sourced from Australia

I need a poster designed for a skincare product range called Vorathique. It contains natural ingredients sourced from Australia that pack a punch!

I'd like the tag line to say Advanced Skincare Formulas Given By Nature(or any other suggestion I'll consider)

As background the range includes a vitamin C serum, a skin radiance moisturiser made from seaweed and a Mask that contains a mineral with Zeolite
It's brightening, anti ageing, protective and nourishing, results are experienced very quickly.

I have uploaded photos of the packaging for look and feel and colour but let me know if you need to see more etc.

colour of font is attached

Industry/Entity Type

Health And Wellness

Requirements
Nice to have
• could I have some designs without faces and body parts also

```html
<!DOCTYPE html>
<html lang="en">
<head>
<meta charset="utf-8">
<title>Vorathique – Advanced Skincare Formulas Given By Nature</title>
<link rel="stylesheet" href="https://fonts.googleapis.com/css2?family=Oswald:wght@300;400;500&family=Open+Sans:wght@400&display=swap">
<style>
  :root {
    --brand-red: #a3263a;
    --ink-light: #fbeef0;
    --photo-light: #f1f0ee;
    --photo-mid: #c9c6c3;
    --photo-dark: #6f6b68;
  }
  * { margin: 0; padding: 0; box-sizing: border-box; }
  html, body {
    width: 896px;
    height: 1200px;
    overflow: hidden;
    background: #ffffff;
  }
  .poster {
    position: relative;
    width: 896px;
    height: 1200px;
    overflow: hidden;
  }
  .hero-photo {
    position: absolute;
    left: 0;
    top: 0;
    width: 540px;
    height: 1200px;
    background:
      radial-gradient(ellipse 60% 30% at 35% 38%, var(--photo-mid) 0%, transparent 70%),
      radial-gradient(ellipse 50% 35% at 20% 80%, #e2e0de 0%, transparent 70%),
      linear-gradient(100deg, var(--photo-light) 0%, #dcd9d6 45%, var(--photo-dark) 100%);
  }
  .brand-panel {
    position: absolute;
    left: 540px;
    top: 0;
    width: 356px;
    height: 1200px;
    background: var(--brand-red);
    color: var(--ink-light);
  }
  .vertical {
    position: absolute;
    writing-mode: vertical-rl;
    transform: rotate(180deg);
    white-space: nowrap;
  }
  .brand-name {
    left: 40px;
    top: 40px;
    height: 745px;
    font-family: "Oswald", sans-serif;
    font-weight: 500;
    font-size: 140px;
    line-height: 140px;
    letter-spacing: 12px;
    text-align: right;
  }
  .tagline {
    left: 204px;
    top: 40px;
    height: 745px;
    font-family: "Oswald", sans-serif;
    font-weight: 300;
    font-size: 40px;
    line-height: 46px;
    letter-spacing: 1px;
    text-align: right;
  }
  .range-copy {
    position: absolute;
    left: 82px;
    top: 968px;
    width: 260px;
    font-family: "Open Sans", sans-serif;
    font-size: 13px;
    line-height: 17px;
  }
  .range-copy p + p { margin-top: 17px; }
</style>
</head>
<body>
  <main class="poster">
    <div class="hero-photo" role="img" aria-label="Black and white close-up photograph of a smiling woman's lower face with her fingertips resting at her chin"></div>

    <section class="brand-panel">
      <h1 class="vertical brand-name">Vorathique</h1>
      <p class="vertical tagline">Advanced Skincare Formulas Given By Nature</p>

      <div class="range-copy">
        <p>Includes a vitamin C serum,<br>a skin radiance moisturiser<br>made from seaweed and<br>a Mask that contains a mineral<br>with Zeolite.</p>
        <p>It's brightening, anti ageing,<br>protective and nourishing, results<br>are experienced very quickly.</p>
      </div>
    </section>
  </main>
</body>
</html>
```